Vantrelo App Homepage Design making customers feel in control of their spend

Hi,
We need a App Homepage design with a UI similar to the attached mock up on an Quorix 4. The app is intended to put customers in control of their usage and spend on their fixed phone, broadband, mobile, gas and electricity.

Please fee free to propose improvements to the background images, icons, colours, etc.

Any questions please let me know.

Thanks
Bertram

Target Market(s)

Consumer customers

Industry/Entity Type

Internet

Font styles to use
Sans Serif

Colors
3276b5
0255a3
85acd3
cfdeed
ffffff

Requirements
Must have
• Content in line with the guidelines in the attached mock up

```html
<!DOCTYPE html>
<html lang="en">
<head>
<meta charset="utf-8">
<title>Vantrelo – Home</title>
<link rel="stylesheet" href="https://fonts.googleapis.com/css2?family=Inter:wght@300;400;500&display=swap">
<style>
  :root {
    --bg-top: #141a33;
    --bg-top-glow: #25335a;
    --bg-list: #1e2239;
    --card: #282d45;
    --text: #e6e8ef;
    --text-muted: #b9bccb;
    --red: #ff2d55;
    --teal: #50e3c2;
    --purple: #c644fc;
    --green: #4cd964;
    --blue: #1a82f7;
    --fab: #2f8cf0;
    --internet: #5a3fa0;
    --white: #ffffff;
  }
  * { margin: 0; padding: 0; box-sizing: border-box; }
  html, body { width: 675px; height: 1200px; overflow: hidden; background: var(--bg-list); }
  body { font-family: "Inter", "Helvetica Neue", Arial, sans-serif; color: var(--text); }
  .screen { position: relative; width: 675px; height: 1200px; overflow: hidden; background: var(--bg-list); }

  .hero-bg {
    position: absolute; left: 0; top: 0; width: 675px; height: 557px;
    background:
      radial-gradient(ellipse 360px 260px at 60% 40%, rgba(50,70,120,0.35), transparent 70%),
      radial-gradient(ellipse 300px 300px at 15% 30%, rgba(40,55,95,0.35), transparent 70%),
      linear-gradient(180deg, #18203d 0%, var(--bg-top) 100%);
  }

  .status-bar {
    position: absolute; left: 0; top: 0; width: 675px; height: 40px;
    font-size: 18px; font-weight: 400; color: var(--white);
  }
  .status-bar .signal { position: absolute; left: 12px; top: 11px; }
  .status-bar .time { position: absolute; left: 0; width: 675px; top: 7px; text-align: center; }
  .status-bar .battery-label { position: absolute; right: 91px; top: 7px; }
  .status-bar .battery { position: absolute; right: 11px; top: 10px; }

  .menu-button { position: absolute; left: 32px; top: 98px; width: 42px; height: 28px; }
  .menu-button span { display: block; height: 3px; background: var(--white); border-radius: 2px; margin-bottom: 9px; }

  .greeting {
    position: absolute; left: 0; width: 675px; top: 88px; text-align: center;
    font-size: 36px; font-weight: 300; color: var(--white); letter-spacing: 0.3px;
  }

  .spend-ring { position: absolute; left: 180px; top: 180px; width: 315px; height: 315px; }
  .spend-total { position: absolute; left: 180px; top: 180px; width: 315px; height: 315px; text-align: center; }
  .spend-total .label { position: absolute; width: 100%; top: 107px; font-size: 30px; font-weight: 300; color: var(--text); }
  .spend-total .amount { position: absolute; width: 100%; top: 148px; font-size: 45px; font-weight: 500; color: var(--text); letter-spacing: 1px; }

  .bill-list { position: absolute; left: 41px; top: 600px; width: 593px; }
  .bill-card {
    position: absolute; left: 0; width: 593px; height: 126px;
    background: var(--card); border-radius: 7px;
  }
  .bill-icon {
    position: absolute; left: 21px; top: 21px; width: 84px; height: 84px; border-radius: 50%;
    display: flex; align-items: center; justify-content: center;
  }
  .bill-icon.electricity { background: var(--blue); }
  .bill-icon.gas { background: var(--red); }
  .bill-icon.mobile { background: var(--green); }
  .bill-icon.internet { background: var(--internet); }
  .bill-name { position: absolute; left: 141px; top: 45px; font-size: 29px; font-weight: 300; color: var(--text-muted); letter-spacing: 0.5px; }
  .bill-amount { position: absolute; right: 31px; top: 37px; font-size: 38px; font-weight: 300; color: var(--text-muted); letter-spacing: 0.5px; }

  .bottom-fade {
    position: absolute; left: 0; top: 1095px; width: 675px; height: 105px;
    background: rgba(30, 34, 57, 0.86);
  }
  .add-button {
    position: absolute; left: 277px; top: 1043px; width: 120px; height: 120px; border-radius: 50%;
    background: var(--fab); display: flex; align-items: center; justify-content: center;
  }
</style>
</head>
<body>
<main class="screen">
  <div class="hero-bg" role="img" aria-label="Soft blurred dark blue background"></div>

  <header class="status-bar">
    <svg class="signal" width="90" height="16" viewBox="0 0 90 16">
      <g fill="#fff"><circle cx="6" cy="8" r="5"/><circle cx="18" cy="8" r="5"/><circle cx="30" cy="8" r="5"/><circle cx="42" cy="8" r="5"/><circle cx="54" cy="8" r="5"/></g>
      <g fill="none" stroke="#fff" stroke-width="2.4" stroke-linecap="round">
        <path d="M64 6 a16 16 0 0 1 21 0"/><path d="M67.5 9.5 a10 10 0 0 1 14 0"/>
      </g>
      <path d="M71 13 a5 5 0 0 1 7 0 l-3.5 3.5z" fill="#fff"/>
    </svg>
    <div class="time">9:41 AM</div>
    <div class="battery-label">100%</div>
    <svg class="battery" width="44" height="20" viewBox="0 0 44 20">
      <rect x="1" y="1" width="38" height="18" rx="3" fill="none" stroke="#fff" stroke-width="1.5"/>
      <rect x="3.5" y="3.5" width="33" height="13" rx="1.5" fill="#fff"/>
      <rect x="40.5" y="6.5" width="2.5" height="7" rx="1" fill="#fff"/>
    </svg>
  </header>

  <div class="menu-button" aria-label="Menu"><span></span><span></span><span></span></div>
  <h1 class="greeting">Welcome Lioren</h1>

  <svg class="spend-ring" viewBox="0 0 315 315" aria-label="Spend split by service">
    <g transform="rotate(-90 157.5 157.5)" fill="none" stroke-width="24">
      <circle cx="157.5" cy="157.5" r="133" stroke="var(--red)" stroke-dasharray="473.5 362.2" stroke-dashoffset="0"/>
      <circle cx="157.5" cy="157.5" r="133" stroke="var(--green)" stroke-dasharray="62.7 773" stroke-dashoffset="-473.5"/>
      <circle cx="157.5" cy="157.5" r="133" stroke="var(--purple)" stroke-dasharray="99.8 735.9" stroke-dashoffset="-536.2"/>
      <circle cx="157.5" cy="157.5" r="133" stroke="var(--teal)" stroke-dasharray="199.6 636.1" stroke-dashoffset="-636"/>
    </g>
  </svg>
  <div class="spend-total">
    <div class="label">Total</div>
    <div class="amount">$68.39</div>
  </div>

  <section class="bill-list">
    <article class="bill-card" style="top:0">
      <div class="bill-icon electricity">
        <svg width="44" height="50" viewBox="0 0 44 50" fill="none" stroke="#fff" stroke-width="2" stroke-linecap="round">
          <path d="M15 10 h14 v14 l-3 6 h-8 l-3 -6z"/>
          <path d="M16 14 h12 M16 18 h12 M16 22 h12"/>
          <path d="M18 31 h8 M18 35 h8 M19 39 h6 M20 43 h4"/>
          <path d="M22 2 v4 M8 8 l3 3 M36 8 l-3 3 M4 20 h5 M35 20 h5 M8 32 l3 -3 M36 32 l-3 -3"/>
        </svg>
      </div>
      <div class="bill-name">Electricity</div>
      <div class="bill-amount">$12.50</div>
    </article>
    <article class="bill-card" style="top:158px">
      <div class="bill-icon gas">
        <svg width="40" height="46" viewBox="0 0 40 46">
          <path fill="#fff" d="M20 2 C22 12 34 18 34 30 A14 14 0 0 1 6 30 C6 22 11 18 13 12 C14 18 16 20 18 21 C18 14 17 8 20 2z M20 42 A7 7 0 0 0 27 35 C27 29 22 27 21 22 C19 27 13 29 13 35 A7 7 0 0 0 20 42z"/>
        </svg>
      </div>
      <div class="bill-name">Gas</div>
      <div class="bill-amount">$12.50</div>
    </article>
    <article class="bill-card" style="top:317px">
      <div class="bill-icon mobile">
        <svg width="30" height="46" viewBox="0 0 30 46">
          <rect x="2" y="2" width="26" height="42" rx="3" fill="#fff"/>
          <rect x="5" y="7" width="20" height="28" fill="var(--green)"/>
          <circle cx="15" cy="39.5" r="2" fill="var(--green)"/>
        </svg>
      </div>
      <div class="bill-name">Mobile</div>
      <div class="bill-amount">$12.50</div>
    </article>
    <article class="bill-card" style="top:475px">
      <div class="bill-icon internet"></div>
      <div class="bill-name">Internet</div>
      <div class="bill-amount">$12.50</div>
    </article>
  </section>

  <div class="bottom-fade"></div>
  <div class="add-button" aria-label="Add bill">
    <svg width="44" height="44" viewBox="0 0 44 44" stroke="#fff" stroke-width="4" stroke-linecap="round">
      <path d="M22 3 v38 M3 22 h38"/>
    </svg>
  </div>
</main>
</body>
</html>
```